Penwhistle & Partners - stylish and sophisticated box design required!

We need a packaging design for our online training company based in Australia called 'Penwhistle & Partners'. We will be sending out Slate Lite`s as well as an A4 ring bound document of 60 pages. We would like the Slate to sit at the bottom of the box with the A4 document sitting on top. Inside the box, there will be fine paper covering the product. Maybe we could have a pattern or the logo on this.

The design should be a cardboard pull out box, black in colour with the logo embossed on the cover (attached institute logo). We are looking for the packaging to communicate sophistication and style.
An examples of a cardboard box shape we quite like could be found on this site:

http://tasks.brieflane-example.com.au/task.aspx?id=71305

I have uploaded two different logos as the previous logo was not nice!

Industry/Entity Type

It Company

```html
<!DOCTYPE html>
<html lang="en">
<head>
<meta charset="utf-8">
<title>Penwhistle &amp; Partners – Pull-out Box Packaging</title>
<link href="https://fonts.googleapis.com/css2?family=Cinzel:wght@500&display=swap" rel="stylesheet">
<style>
  :root {
    --page: #ffffff;
    --sleeve: #4c4b52;
    --sleeve-light: #57565d;
    --sleeve-fold: #6e6d74;
    --seal-ink: #ffffff;
    --tray: #e1b2b0;
    --tray-light: #e8c2c0;
    --tray-fold: #f1d3d2;
    --ribbon: #1e1e20;
    --tissue: #4f4e55;
    --tissue-light: #5a5960;
    --tissue-deep: #424148;
    --tissue-ink: #2a292e;
  }
  * { margin: 0; padding: 0; box-sizing: border-box; }
  html, body { width: 1200px; height: 1102px; overflow: hidden; background: var(--page); }
  .canvas { position: relative; width: 1200px; height: 1102px; }

  .brand-name {
    font-family: "Cinzel", "Times New Roman", serif;
    font-weight: 500; letter-spacing: 1px; text-align: center;
  }

  /* Outer sleeve net */
  .sleeve { position: absolute; left: 24px; top: 35px; width: 339px; height: 1067px; }
  .sleeve svg { display: block; }
  .sleeve-seal {
    position: absolute; left: 67px; top: 296px; width: 206px; height: 206px;
    border-radius: 50%; border: 2px solid var(--seal-ink);
    display: flex; align-items: center; justify-content: center;
  }
  .sleeve-seal .brand-name { font-size: 19px; line-height: 1.3; color: var(--seal-ink); }

  /* Inner tray net */
  .tray { position: absolute; left: 458px; top: 13px; }
  .tray svg { display: block; }

  /* Tissue paper sheet */
  .tissue {
    position: absolute; left: 413px; top: 596px; width: 766px; height: 462px;
    overflow: hidden;
    background:
      linear-gradient(62deg, transparent 40%, rgba(255,255,255,0.04) 41%, transparent 55%),
      linear-gradient(118deg, transparent 30%, rgba(0,0,0,0.06) 31%, transparent 48%),
      linear-gradient(28deg, transparent 58%, rgba(255,255,255,0.035) 59%, transparent 72%),
      radial-gradient(circle at 30% 35%, var(--tissue-light), transparent 60%),
      linear-gradient(135deg, var(--tissue), var(--tissue-deep));
  }
  .tissue-seal {
    position: absolute; left: var(--x); top: var(--y);
    width: 148px; height: 148px; border-radius: 50%;
    border: 2px solid var(--tissue-ink);
    display: flex; align-items: center; justify-content: center;
  }
  .tissue-seal .brand-name { font-size: 13px; line-height: 1.3; color: var(--tissue-ink); }
</style>
</head>
<body>
<main class="canvas">

  <section class="sleeve" aria-label="Outer sleeve">
    <svg width="339" height="1067" viewBox="0 0 339 1067">
      <defs>
        <linearGradient id="sleeveShade" x1="0" y1="0" x2="1" y2="1">
          <stop offset="0" stop-color="var(--sleeve-light)"/>
          <stop offset="1" stop-color="var(--sleeve)"/>
        </linearGradient>
      </defs>
      <path class="sleeve-glue-tab" d="M6 0 H333 L339 8 V17 H0 V8 Z" fill="var(--sleeve)"/>
      <rect class="sleeve-body" x="0" y="17" width="339" height="1050" fill="url(#sleeveShade)"/>
      <g stroke="var(--sleeve-fold)" stroke-width="1">
        <line x1="0" y1="17" x2="339" y2="17"/>
        <line x1="0" y1="80" x2="339" y2="80"/>
        <line x1="0" y1="543" x2="339" y2="543"/>
        <line x1="0" y1="605" x2="339" y2="605"/>
      </g>
    </svg>
    <div class="sleeve-seal">
      <span class="brand-name">Penwhistle<br>&amp;<br>Partners</span>
    </div>
  </section>

  <section class="tray" aria-label="Inner tray">
    <svg width="654" height="531" viewBox="0 0 654 531">
      <g class="tray-panels">
        <rect x="94" y="0" width="463" height="29" fill="var(--tray-light)"/>
        <rect x="94" y="29" width="463" height="65" fill="var(--tray)"/>
        <path d="M94 29 V94 H49 V75 L40 68 V45 Z" fill="var(--tray)"/>
        <path d="M557 29 V94 H602 V75 L611 68 V45 Z" fill="var(--tray)"/>
        <rect x="94" y="94" width="463" height="343" fill="var(--tray)"/>
        <rect x="0" y="96" width="29" height="339" fill="var(--tray-light)"/>
        <rect x="29" y="96" width="65" height="339" fill="var(--tray)"/>
        <rect x="625" y="96" width="29" height="339" fill="var(--tray-light)"/>
        <rect x="557" y="96" width="68" height="339" fill="var(--tray)"/>
        <rect x="94" y="437" width="463" height="65" fill="var(--tray)"/>
        <rect x="94" y="502" width="463" height="29" fill="var(--tray-light)"/>
        <path d="M94 437 V502 H40 V489 L49 482 V456 Z" fill="var(--tray)"/>
        <path d="M557 437 V502 H611 V489 L602 482 V456 Z" fill="var(--tray)"/>
      </g>
      <g class="tray-folds" stroke="var(--tray-fold)" stroke-width="1" fill="none">
        <line x1="94" y1="29" x2="557" y2="29"/>
        <line x1="94" y1="94" x2="557" y2="94"/>
        <line x1="94" y1="437" x2="557" y2="437"/>
        <line x1="94" y1="502" x2="557" y2="502"/>
        <line x1="94" y1="29" x2="94" y2="502"/>
        <line x1="557" y1="29" x2="557" y2="502"/>
        <line x1="29" y1="96" x2="29" y2="435"/>
        <line x1="625" y1="96" x2="625" y2="435"/>
      </g>
      <path class="pull-ribbon" d="M9 258 H62 V278 H9 Z" fill="var(--ribbon)"/>
    </svg>
  </section>

  <section class="tissue" aria-label="Tissue paper wrap">
    <div class="tissue-seal" style="--x:4px;--y:-38px"><span class="brand-name">Penwhistle<br>&amp;<br>Partners</span></div>
    <div class="tissue-seal" style="--x:221px;--y:-38px"><span class="brand-name">Penwhistle<br>&amp;<br>Partners</span></div>
    <div class="tissue-seal" style="--x:443px;--y:-38px"><span class="brand-name">Penwhistle<br>&amp;<br>Partners</span></div>
    <div class="tissue-seal" style="--x:665px;--y:-38px"><span class="brand-name">Penwhistle<br>&amp;<br>Partners</span></div>

    <div class="tissue-seal" style="--x:-108px;--y:70px"><span class="brand-name">Penwhistle<br>&amp;<br>Partners</span></div>
    <div class="tissue-seal" style="--x:113px;--y:70px"><span class="brand-name">Penwhistle<br>&amp;<br>Partners</span></div>
    <div class="tissue-seal" style="--x:334px;--y:70px"><span class="brand-name">Penwhistle<br>&amp;<br>Partners</span></div>
    <div class="tissue-seal" style="--x:556px;--y:70px"><span class="brand-name">Penwhistle<br>&amp;<br>Partners</span></div>

    <div class="tissue-seal" style="--x:4px;--y:179px"><span class="brand-name">Penwhistle<br>&amp;<br>Partners</span></div>
    <div class="tissue-seal" style="--x:221px;--y:179px"><span class="brand-name">Penwhistle<br>&amp;<br>Partners</span></div>
    <div class="tissue-seal" style="--x:443px;--y:179px"><span class="brand-name">Penwhistle<br>&amp;<br>Partners</span></div>
    <div class="tissue-seal" style="--x:665px;--y:179px"><span class="brand-name">Penwhistle<br>&amp;<br>Partners</span></div>

    <div class="tissue-seal" style="--x:-108px;--y:288px"><span class="brand-name">Penwhistle<br>&amp;<br>Partners</span></div>
    <div class="tissue-seal" style="--x:113px;--y:288px"><span class="brand-name">Penwhistle<br>&amp;<br>Partners</span></div>
    <div class="tissue-seal" style="--x:334px;--y:288px"><span class="brand-name">Penwhistle<br>&amp;<br>Partners</span></div>
    <div class="tissue-seal" style="--x:556px;--y:288px"><span class="brand-name">Penwhistle<br>&amp;<br>Partners</span></div>

    <div class="tissue-seal" style="--x:4px;--y:396px"><span class="brand-name">Penwhistle<br>&amp;<br>Partners</span></div>
    <div class="tissue-seal" style="--x:221px;--y:396px"><span class="brand-name">Penwhistle<br>&amp;<br>Partners</span></div>
    <div class="tissue-seal" style="--x:443px;--y:396px"><span class="brand-name">Penwhistle<br>&amp;<br>Partners</span></div>
    <div class="tissue-seal" style="--x:665px;--y:396px"><span class="brand-name">Penwhistle<br>&amp;<br>Partners</span></div>
  </section>

</main>
</body>
</html>
```